Need simple and modern looking business card with all my information on one side and logo on the other side
Info :
Company name - VELMAR CONSTRUCTION LLC
Company addres- 418 harbor 87th. Dunmoor park ny 10352
Email- velmarllc@tridomail.Com
Company phone number 555-318-6094
Cell number- 555-742-0583
Web site - velmarllc.Com
My name Gerald tomasino

Target Market(s)

Construction , home improvement, remodeling

Industry/Entity Type

Construction

Contact Information for Business Card

It has to be moder but at the same time simple

Font styles to use
Sans Serif

Colors
0255a3
ffffff
000000
f78f20
b1b1b1
9d9d9d
1b1b1b
33a6d7
ec1f27

Requirements
Must have
• My logo on one side maybe with a some kind of background on the other side all my information
Nice to have
• Some kind of background pictures provided by you .PLEASE HAVE ACCOUNT WITH PIXELVAULT WILL NOT PAY ANY EXTRA FEES .
Should not have
• Any kind of hamer, nails,screws, helmets itp. Please do not copy the other designs come up with something new.

```html
<!DOCTYPE html>
<html lang="en">
<head>
<meta charset="utf-8">
<title>Velmar Construction LLC — Business Card</title>
<link rel="stylesheet" href="https://fonts.googleapis.com/css2?family=Open+Sans:wght@400;600;700&display=swap">
<style>
  :root {
    --brand-blue: #1570b8;
    --brand-blue-deep: #0255a3;
    --brand-red: #ec1f27;
    --brand-orange: #f78f20;
    --ink: #1b1b1b;
    --text-grey: #4a4a4a;
    --paper: #ffffff;
    --backdrop: #e9ebeb;
  }
  * { box-sizing: border-box; margin: 0; padding: 0; }
  html, body {
    width: 1200px; height: 1200px; overflow: hidden;
    background: var(--backdrop);
    font-family: "Open Sans", Arial, sans-serif;
  }
  .sheet {
    width: 1200px; height: 1200px;
    display: flex; flex-direction: column;
    align-items: center; justify-content: center; gap: 70px;
  }
  .card {
    width: 860px; height: 491px;
    position: relative; overflow: hidden;
    box-shadow: 0 10px 28px rgba(0,0,0,0.14);
  }
  /* Information side */
  .card--front { background: var(--paper); }
  .front__brand {
    position: absolute; left: 80px; top: 120px;
    display: flex; align-items: center; gap: 14px;
  }
  .brand-mark {
    width: 22px; height: 22px; background: var(--brand-orange);
  }
  .brand-name {
    font-size: 38px; font-weight: 600; color: var(--ink); letter-spacing: 1px;
  }
  .front__person {
    position: absolute; left: 80px; top: 205px;
    font-size: 30px; font-weight: 700; color: var(--brand-red); letter-spacing: 0.5px;
  }
  .front__contacts {
    position: absolute; left: 80px; top: 260px;
    font-size: 21px; line-height: 36px; color: var(--text-grey);
  }
  .label { color: var(--brand-red); }
  .divider { color: var(--text-grey); padding: 0 6px; }
  .front__rule {
    position: absolute; left: 0; right: 0; bottom: 94px;
    height: 3px; background: var(--brand-blue);
  }
  .front__band {
    position: absolute; left: 0; right: 0; bottom: 0; height: 84px;
    background: var(--brand-blue);
    display: flex; align-items: center; padding-left: 80px;
    color: var(--paper); font-size: 22px;
  }
  /* Logo side */
  .card--back {
    background: radial-gradient(ellipse at 40% 35%, #1a7cc4 0%, var(--brand-blue) 45%, var(--brand-blue-deep) 100%);
    display: flex; align-items: center; justify-content: center;
  }
  .back__name {
    color: var(--paper); font-size: 52px; font-weight: 600; letter-spacing: 3px;
  }
</style>
</head>
<body>
  <main class="sheet">
    <section class="card card--front" aria-label="Business card, information side">
      <div class="front__brand">
        <span class="brand-mark"></span>
        <span class="brand-name">VELMAR CONSTRUCTION LLC</span>
      </div>
      <p class="front__person">GERALD TOMASINO</p>
      <div class="front__contacts">
        <p><span class="label">T.</span> 555-318-6094<span class="divider">|</span><span class="label">M.</span> 555-742-0583</p>
        <p><span class="label">W.</span> velmarllc.Com<span class="divider">|</span><span class="label">E.</span> velmarllc@tridomail.Com</p>
      </div>
      <div class="front__rule"></div>
      <div class="front__band">418 harbor 87th. Dunmoor park ny 10352</div>
    </section>

    <section class="card card--back" aria-label="Business card, logo side">
      <span class="back__name">VELMAR CONSTRUCTION LLC</span>
    </section>
  </main>
</body>
</html>
```